Construction Company Needs Letterhead Design

We recently had a new logo designed and would like to have our letterhead updated to a trendier design. We are a concrete construction company based out of Iowa, but do work for Agricultural businesses across the Midwest.

Industry/Entity Type

Construction

Colors
ec1f27
000000
ffffff

Requirements
Must have
• Must stay within our current color scheme of red/black/white. Must have have our address, phone number, e-mail address, etc. printed on the letterhead as well.

```html
<!DOCTYPE html>
<html lang="en">
<head>
<meta charset="utf-8">
<title>Harlan Ridge, Inc. Letterhead</title>
<link href="https://fonts.googleapis.com/css2?family=Open+Sans:wght@400;700&display=swap" rel="stylesheet">
<style>
  :root {
    --brand-red: #ec1f27;
    --brand-black: #000000;
    --ink-dark: #2b2b2b;
    --ink-grey: #555555;
    --bar-grey: #4a4a4a;
    --paper: #ffffff;
    --backdrop: #dcdcdc;
  }
  * { margin: 0; padding: 0; box-sizing: border-box; }
  html, body { width: 1200px; height: 784px; overflow: hidden; }
  body {
    background: var(--backdrop);
    font-family: "Open Sans", Arial, sans-serif;
    display: flex; align-items: center; justify-content: center;
  }
  .letterhead {
    position: relative;
    width: 572px; height: 740px;
    background: var(--paper);
    box-shadow: 0 2px 10px rgba(0,0,0,0.12);
  }
  .corner-mark { position: absolute; top: 0; display: flex; gap: 3px; }
  .corner-mark--left { left: 0; }
  .corner-mark--right { right: 0; }
  .corner-mark span { display: block; width: 26px; height: 5px; }
  .corner-mark .mark-grey { background: var(--bar-grey); }
  .corner-mark .mark-red { background: var(--brand-red); }

  .brand {
    position: absolute; top: 58px; right: 44px;
    display: flex; align-items: center; gap: 9px;
  }
  .brand-square { width: 22px; height: 22px; background: var(--brand-red); }
  .brand-name {
    font-weight: 700; font-size: 22px; letter-spacing: 0.5px;
    color: var(--ink-dark); text-transform: uppercase;
  }

  .footer { position: absolute; left: 0; bottom: 0; width: 572px; height: 80px; }
  .footer-stripes { position: absolute; inset: 0; }
  .contact-row {
    position: absolute; left: 10px; top: 6px;
    display: flex; align-items: center; gap: 9px;
    font-size: 8.5px; line-height: 1; color: var(--ink-grey);
    white-space: nowrap;
  }
  .contact-item { display: flex; align-items: center; gap: 3px; }
  .contact-icon { width: 9px; height: 9px; flex: none; }
  .website {
    position: absolute; right: 14px; bottom: 9px;
    font-weight: 700; font-size: 10.5px; line-height: 1; color: var(--paper);
    white-space: nowrap;
  }
</style>
</head>
<body>
  <main class="letterhead">
    <div class="corner-mark corner-mark--left"><span class="mark-red"></span><span class="mark-grey"></span></div>
    <div class="corner-mark corner-mark--right"><span class="mark-grey"></span><span class="mark-red"></span></div>

    <header class="brand">
      <span class="brand-square"></span>
      <span class="brand-name">Harlan Ridge, Inc.</span>
    </header>

    <footer class="footer">
      <svg class="footer-stripes" width="572" height="80" viewBox="0 0 572 80">
        <polygon points="0,26 150,26 147,30 0,30" fill="var(--brand-red)"/>
        <polygon points="156,26 300,26 297,30 153,30" fill="var(--brand-red)"/>
        <polygon points="306,26 440,26 437,30 303,30" fill="var(--brand-red)"/>
        <polygon points="0,36 150,36 144,44 0,44" fill="var(--bar-grey)"/>
        <polygon points="154,36 300,36 294,44 148,44" fill="var(--bar-grey)"/>
        <polygon points="304,36 420,36 414,44 298,44" fill="var(--bar-grey)"/>
        <polygon points="0,48 420,48 440,36 572,36 572,80 0,80" fill="var(--ink-dark)"/>
      </svg>
      <div class="contact-row">
        <span class="contact-item">
          <svg class="contact-icon" viewBox="0 0 10 10"><circle cx="5" cy="5" r="5" fill="var(--brand-red)"/><path d="M5 2.2a1.8 1.8 0 0 1 1.8 1.8C6.8 5.3 5 7.8 5 7.8S3.2 5.3 3.2 4A1.8 1.8 0 0 1 5 2.2z" fill="#fff"/></svg>
          2140 Prairie View Road Suite 100, Ames IA 50010
        </span>
        <span class="contact-item">
          <svg class="contact-icon" viewBox="0 0 10 10"><circle cx="5" cy="5" r="5" fill="var(--brand-red)"/><path d="M3.2 2.5h1l.5 1.3-.6.5a3.6 3.6 0 0 0 1.6 1.6l.5-.6 1.3.5v1c0 .3-.3.6-.6.6A4.4 4.4 0 0 1 2.6 3.1c0-.3.3-.6.6-.6z" fill="#fff"/></svg>
          (515) 555-0142
        </span>
        <span class="contact-item">
          <svg class="contact-icon" viewBox="0 0 10 10"><circle cx="5" cy="5" r="5" fill="var(--brand-red)"/><rect x="2.4" y="3.2" width="5.2" height="3.6" fill="#fff"/><path d="M2.4 3.2 5 5.3l2.6-2.1" fill="none" stroke="var(--brand-red)" stroke-width="0.6"/></svg>
          info@harlanridgeservices.com
        </span>
      </div>
      <div class="website">www.harlanridgeservices.com</div>
    </footer>
  </main>
</body>
</html>
```